Postcard, Logo, and Website Design for Direct to Consumer Personal Bankruptcy Service

We are launching a bankruptcy legal practice. Our postcard design will be mailed to prospective clients who have already been sued by their credit card companies.

We would like people to glean from the post card that they can call to set up a no-fee consultation, or to phone our offices, where our receptionist can aid them in setting up a no-fee consultation.

Logo should be professional, but not overly stuffy.

Website copy can be added later, but most important is a space where people can fill out there info so we can reach out to them.

Pertinent info that should be on postcard

Name: Harbor Pines Debt Relief
Phone: 616-392-7158
Website: HPDebtRelief.example

Rough ideas that we've tossed around include the following (but use your own judgement - we're counting on you for creativity):

Creditors Calling?
Mountain of Debt?
Getting Sued?

We can help!

Target Market(s)

People who are thinking about bankruptcy and have already been sued

Industry/Entity Type

Financial Service

Logo Text

Harbor Pines Debt Relief

Number of Pages Required

1 page

Font styles to use
Sans Serif

Colors

Designer to choose colors to be used in the design.

Requirements
Must have
• Space for info about bankruptcy process
• Space for user to submit info

```html
<!DOCTYPE html>
<html lang="en">
<head>
<meta charset="utf-8">
<title>Harbor Pines Debt Relief – Postcard</title>
<link href="https://fonts.googleapis.com/css2?family=Oswald:wght@300;400;600;700&family=Open+Sans:wght@400;600&display=swap" rel="stylesheet">
<style>
  :root{
    --blue:#2a8fd6;
    --navy:#1e3f9c;
    --ink:#2b2d33;
    --charcoal:#36373b;
    --paper:#ffffff;
    --bg:#e4e5e7;
    --photo-a:#d9d6d0;
    --photo-b:#9aa3ad;
    --yellow:#f4cf1f;
  }
  *{box-sizing:border-box;margin:0;padding:0}
  html,body{width:1200px;height:1200px;overflow:hidden;background:var(--bg)}
  body{position:relative;font-family:"Open Sans",Arial,sans-serif}
  .card{position:absolute;left:210px;width:780px;height:520px;background:var(--paper);overflow:hidden;box-shadow:0 4px 14px rgba(0,0,0,.18)}
  .card--back{top:50px}
  .card--front{top:630px}
  .photo{position:absolute}
  .brand{position:absolute;font-family:"Oswald",sans-serif;font-weight:600;color:var(--blue);font-size:40px;letter-spacing:-.5px;line-height:1}
  .badge{position:absolute}
  .badge text{font-family:"Oswald",sans-serif;fill:#fff;text-anchor:middle}

  /* back side */
  .back-photo{left:0;top:0;width:590px;height:320px;background:linear-gradient(135deg,var(--photo-a),#c8c4bd 55%,var(--photo-b))}
  .back-photo .accent{position:absolute;right:0;top:230px;width:50px;height:80px;background:var(--yellow)}
  .back-band{position:absolute;left:0;top:0;width:590px;height:520px}
  .about{position:absolute;left:38px;top:322px;width:330px;color:#fff}
  .about h2{font-family:"Oswald",sans-serif;font-weight:400;font-size:20px;line-height:1.2;margin-bottom:6px}
  .about p{font-size:10.5px;line-height:1.4}
  .call{position:absolute;left:400px;top:392px;color:#fff;font-family:"Oswald",sans-serif}
  .call .label{font-weight:300;font-size:22px;display:block}
  .call .phone{font-weight:400;font-size:26px;color:var(--ink)}
  .footer{position:absolute;left:0;bottom:0;width:400px;height:62px;background:var(--charcoal);padding:12px 40px;color:#fff}
  .footer .name{font-family:"Oswald",sans-serif;font-size:15px;color:var(--blue);text-transform:uppercase}
  .footer .url{font-size:12px;margin-top:3px}
  .mail-side{position:absolute;left:590px;top:0;width:190px;height:520px}
  .stamp{position:absolute;right:28px;top:28px;width:62px;height:74px;border:1.5px solid var(--ink)}
  .address-line{position:absolute;left:22px;width:146px;height:1px;background:#999}

  /* front side */
  .front-photo{left:180px;top:0;width:600px;height:225px;background:linear-gradient(120deg,#eef0f2,#b9c4cc 55%,#d6b45a)}
  .person{left:612px;top:118px;width:168px;height:402px;background:linear-gradient(180deg,#c9c4bf,#8f9499 60%,#6f757c)}
  .front-band{position:absolute;left:0;top:0;width:780px;height:520px}
  .questions{position:absolute;left:52px;top:262px;color:#fff;font-size:21px;line-height:1.32}
  .divider{position:absolute;left:302px;top:262px;width:2px;height:92px;background:#fff}
  .help{position:absolute;left:330px;top:250px;font-family:"Oswald",sans-serif;font-weight:700;color:var(--ink);line-height:.92}
  .help .we{font-size:44px;margin-right:10px}
  .help .can{font-size:44px;color:#fff}
  .help .big{font-size:64px;display:block}
  .front-call{position:absolute;left:40px;top:375px;background:#fff;padding:0 8px;font-family:"Oswald",sans-serif;font-size:20px;color:var(--ink);font-weight:300;line-height:1.3}
  .front-call .phone{color:var(--blue);font-weight:400}
</style>
</head>
<body>

<section class="card card--back" aria-label="Postcard back">
  <div class="photo back-photo" role="img" aria-label="Overhead photo of an advisor meeting a young couple at a desk">
    <div class="accent"></div>
  </div>
  <svg class="back-band" viewBox="0 0 590 520">
    <polygon points="0,295 590,330 590,470 400,470 400,520 0,520" fill="#2a8fd6"/>
  </svg>
  <div class="brand" style="left:30px;top:42px">Harbor Pines</div>

  <svg class="badge" style="left:388px;top:250px" width="130" height="130" viewBox="0 0 130 130">
    <g fill="#1e3f9c">
      <rect x="17" y="17" width="96" height="96" transform="rotate(0 65 65)"/>
      <rect x="17" y="17" width="96" height="96" transform="rotate(15 65 65)"/>
      <rect x="17" y="17" width="96" height="96" transform="rotate(30 65 65)"/>
      <rect x="17" y="17" width="96" height="96" transform="rotate(45 65 65)"/>
      <rect x="17" y="17" width="96" height="96" transform="rotate(60 65 65)"/>
      <rect x="17" y="17" width="96" height="96" transform="rotate(75 65 65)"/>
    </g>
    <circle cx="65" cy="65" r="52" fill="none" stroke="#fff" stroke-width="1.5"/>
    <text x="65" y="64" font-size="28" font-weight="700">FREE</text>
    <text x="65" y="86" font-size="15" font-weight="400">CONSULTATION</text>
  </svg>

  <div class="about">
    <h2>ABOUT US</h2>
    <p>Lorem Ipsum is simply dummy text of the printing and typesetting industry. Lorem Ipsum has been the industry's standard dummy text ever since the 1500s, when an unknown printer took a galley of type and scrambled it to make a type specimen book.</p>
  </div>
  <div class="call">
    <span class="label">CALL TOLL FREE</span>
    <span class="phone">616-392-7158</span>
  </div>
  <div class="footer">
    <div class="name">Harbor Pines Debt Relief</div>
    <div class="url">www.HPDebtRelief.example</div>
  </div>

  <div class="mail-side">
    <div class="stamp"></div>
    <div class="address-line" style="top:300px"></div>
    <div class="address-line" style="top:336px"></div>
    <div class="address-line" style="top:372px"></div>
  </div>
</section>

<section class="card card--front" aria-label="Postcard front">
  <div class="photo front-photo" role="img" aria-label="Close-up of a hand holding a tablet and a payment card"></div>
  <svg class="front-band" viewBox="0 0 780 520">
    <polygon points="0,235 780,205 780,360 0,415" fill="#2a8fd6"/>
  </svg>
  <div class="photo person" role="img" aria-label="Cheerful businessman in a grey suit holding banknotes"></div>
  <div class="brand" style="left:30px;top:42px">Harbor Pines</div>

  <svg class="badge" style="left:50px;top:120px" width="120" height="120" viewBox="0 0 130 130">
    <g fill="#1e3f9c">
      <rect x="17" y="17" width="96" height="96" transform="rotate(0 65 65)"/>
      <rect x="17" y="17" width="96" height="96" transform="rotate(15 65 65)"/>
      <rect x="17" y="17" width="96" height="96" transform="rotate(30 65 65)"/>
      <rect x="17" y="17" width="96" height="96" transform="rotate(45 65 65)"/>
      <rect x="17" y="17" width="96" height="96" transform="rotate(60 65 65)"/>
      <rect x="17" y="17" width="96" height="96" transform="rotate(75 65 65)"/>
    </g>
    <text x="65" y="64" font-size="28" font-weight="700">FREE</text>
    <text x="65" y="86" font-size="15" font-weight="400">CONSULTATION</text>
  </svg>

  <div class="questions">Creditors Calling?<br>Mountain of Debt?<br>Getting Sued?</div>
  <div class="divider"></div>
  <div class="help"><span class="we">WE</span><span class="can">CAN</span><span class="big">HELP!</span></div>
  <div class="front-call">CALL TOLL FREE : <span class="phone">616-392-7158</span></div>
</section>

</body>
</html>
```